Business Card & Letterhead Design

We a financial advice company based in Australia. We provide advice to wealthy farmers.

We are changing our business name FROM Brightmere Financial TO Calderstone Wealth and we need a new letterhead and double sided business card design

Attached is designs from our previous branding (Brightmere Financial) as it includes all the details we require on the new Calderstone Wealth business cards and letterhead.

```html
<!DOCTYPE html>
<html lang="en">
<head>
<meta charset="utf-8">
<title>Calderstone Wealth – Letterhead &amp; Business Cards</title>
<link rel="stylesheet" href="https://fonts.googleapis.com/css2?family=Lato:ital,wght@0,300;0,400;0,700;1,300&display=swap">
<style>
  :root {
    --backdrop: #e8e6e3;
    --paper: #ffffff;
    --ink: #454545;
    --ink-soft: #6a6a6a;
    --on-dark: #ffffff;
    --shadow: 0 6px 18px rgba(0,0,0,0.18);
  }
  * { box-sizing: border-box; margin: 0; padding: 0; }
  html, body {
    width: 1200px; height: 1200px; overflow: hidden;
    background: var(--backdrop);
    font-family: "Lato", sans-serif;
    color: var(--ink);
  }
  .stage { position: relative; width: 1200px; height: 1200px; }

  /* Brand lockup */
  .brand { display: flex; flex-direction: column; align-items: center; }
  .brand-row { display: flex; align-items: center; gap: 10px; }
  .brand-dot { border: 2px solid currentColor; border-radius: 50%; flex: none; }
  .brand-name {
    font-family: "Lato", sans-serif; font-weight: 400;
    letter-spacing: 0.06em; text-transform: uppercase; white-space: nowrap;
  }
  .brand-tagline {
    font-weight: 300; text-transform: uppercase; letter-spacing: 0.32em;
    white-space: nowrap;
  }

  /* Letterhead */
  .letterhead {
    position: absolute; left: 60px; top: 150px;
    width: 620px; height: 877px;
    background: var(--paper); box-shadow: var(--shadow);
    display: flex; flex-direction: column;
  }
  .letterhead .brand { margin-top: 70px; color: var(--ink); }
  .letterhead .brand-dot { width: 22px; height: 22px; }
  .letterhead .brand-name { font-size: 30px; }
  .letterhead .brand-tagline { font-size: 11px; margin-top: 6px; }
  .letterhead-body { flex: 1; }
  .letterhead-footer {
    height: 96px; background: var(--ink); color: var(--on-dark);
    display: flex; flex-direction: column; justify-content: center; align-items: center;
    gap: 6px; font-size: 8.5px; letter-spacing: 0.02em;
  }
  .label { font-weight: 700; margin-right: 3px; }
  .sep { margin: 0 6px; }

  /* Business cards */
  .card {
    position: absolute; left: 730px; width: 420px; height: 240px;
    box-shadow: var(--shadow); overflow: hidden;
  }
  .card-front { top: 330px; display: flex; background: var(--paper); }
  .card-front .identity {
    width: 54%; padding: 46px 14px 0 16px; display: flex; flex-direction: column;
  }
  .card-front .brand { align-items: center; color: var(--ink); }
  .card-front .brand-row { gap: 6px; }
  .card-front .brand-dot { width: 11px; height: 11px; border-width: 1.5px; }
  .card-front .brand-name { font-size: 12.5px; letter-spacing: 0.04em; }
  .card-front .brand-tagline { font-size: 5.5px; margin-top: 4px; letter-spacing: 0.28em; }
  .person { margin-top: 40px; padding-left: 4px; }
  .person-name { font-size: 16px; letter-spacing: 0.02em; white-space: nowrap; }
  .person-name .quals { font-size: 7px; margin-left: 4px; letter-spacing: 0; }
  .person-role { font-size: 7px; text-transform: uppercase; line-height: 1.4; margin-top: 3px; }
  .card-front .contact {
    flex: 1; min-width: 0; background: var(--ink); color: var(--on-dark);
    padding: 26px 10px 0 16px; font-size: 10.5px; line-height: 1.5;
    white-space: nowrap;
  }
  .contact p + p { margin-top: 10px; }
  .contact .label { display: inline-block; width: 13px; }

  .card-back {
    top: 610px; background: var(--ink); color: var(--on-dark);
    display: flex; flex-direction: column; align-items: center; padding-top: 40px;
  }
  .card-back .brand { color: var(--on-dark); }
  .card-back .brand-dot { width: 18px; height: 18px; }
  .card-back .brand-name { font-size: 22px; }
  .card-back .brand-tagline { font-size: 8px; margin-top: 4px; }
  .services {
    margin-top: 26px; font-style: italic; font-weight: 300; font-size: 14.5px;
    line-height: 1.6; text-align: center;
  }
  .licensee { margin-top: 22px; font-size: 8.5px; text-align: center; line-height: 1.7; }
</style>
</head>
<body>
<main class="stage">

  <section class="letterhead" aria-label="Letterhead">
    <header class="brand">
      <div class="brand-row">
        <span class="brand-dot"></span>
        <span class="brand-name">Calderstone Wealth</span>
      </div>
      <span class="brand-tagline">Strategic Financial Advice</span>
    </header>
    <div class="letterhead-body"></div>
    <footer class="letterhead-footer">
      <p><span class="label">p</span>(07) 3000 1420<span class="sep">|</span><span class="label">f</span>(07) 3000 1421<span class="sep">|</span><span class="label">m</span>0400 555 218</p>
      <p>Suite 4A, 18 Harlow St Riverton QLD 4100<span class="sep">|</span>PO BOX 5120 Eastvale QLD 4100</p>
      <p>sam@calderstonewealth.com.au<span class="sep">|</span>www.calderstonewealth.com.au</p>
    </footer>
  </section>

  <section class="card card-front" aria-label="Business card front">
    <div class="identity">
      <div class="brand">
        <div class="brand-row">
          <span class="brand-dot"></span>
          <span class="brand-name">Calderstone Wealth</span>
        </div>
        <span class="brand-tagline">Strategic Financial Advice</span>
      </div>
      <div class="person">
        <p class="person-name">SAM GARRICK<span class="quals">B.Ag.Ec. Dip F.P. CFP®</span></p>
        <p class="person-role">Managing Director<br>Authorised Representative</p>
      </div>
    </div>
    <div class="contact">
      <p><span class="label">p</span>(07) 3000 1420<br><span class="label">f</span>(07) 3000 1421<br><span class="label">m</span>0400 555 218</p>
      <p>sam@calderstonewealth.com.au<br>www.calderstonewealth.com.au</p>
      <p>Suite 4A, 18 Harlow St<br>Riverton QLD 4100</p>
      <p>PO BOX 5120<br>Eastvale QLD 4100</p>
    </div>
  </section>

  <section class="card card-back" aria-label="Business card back">
    <div class="brand">
      <div class="brand-row">
        <span class="brand-dot"></span>
        <span class="brand-name">Calderstone Wealth</span>
      </div>
      <span class="brand-tagline">Strategic Financial Advice</span>
    </div>
    <p class="services">Life &amp; TPD Insurance • Income Protection<br>Financial Planning • Retirement Planning</p>
    <p class="licensee">Northgate Advice Partners Limited<br>Australian Financial Services Licensee License Number 581204</p>
  </section>

</main>
</body>
</html>
```